Personal Training

Personal Fitness Trainer
Sports Nutritionist
Individual and Group rates available
Certifications
Global Wellness Coaches Federation
Worldwide Athletic Study Council

Industry/Entity Type

Fitness

Contact Information for Business Card

Dorinda Valcourt
555-284-7160
dvalcourt4@brimfeld.com

```html
<!DOCTYPE html>
<html lang="en">
<head>
<meta charset="utf-8">
<title>Dorinda Valcourt – Personal Training Business Card</title>
<link rel="stylesheet" href="https://fonts.googleapis.com/css2?family=Cinzel:wght@400&family=Comfortaa:wght@400&display=swap">
<style>
  :root {
    --page: #e9e9ec;
    --teal: #0e8ea8;
    --teal-deep: #0a7489;
    --card-light: #f1f1f7;
    --card-tint: #e4e0ef;
    --ink-white: #ffffff;
    --photo-top: #d94a6a;
    --photo-mid: #c98a78;
    --photo-low: #1e1a1c;
  }
  * { margin: 0; padding: 0; box-sizing: border-box; }
  html, body {
    width: 1200px; height: 1000px; overflow: hidden;
    background: var(--page);
  }
  .canvas {
    position: relative; width: 1200px; height: 1000px;
  }
  .card {
    position: absolute; left: 220px; width: 760px; height: 434px;
    overflow: hidden;
    background: linear-gradient(135deg, var(--card-light), var(--card-tint));
    box-shadow: 0 6px 18px rgba(0,0,0,0.18);
  }
  .card--front { top: 44px; }
  .card--back { top: 522px; }
  .card svg.shapes { position: absolute; inset: 0; }
  .background-pattern {
    position: absolute; inset: 0;
    background: linear-gradient(120deg, #f3f2f8 0%, #e8eaf3 45%, #efe6ef 75%, #e5ecf2 100%);
  }
  .photo {
    position: absolute;
    background: linear-gradient(180deg, var(--photo-top) 0%, var(--photo-mid) 45%, var(--photo-top) 62%, var(--photo-low) 80%, var(--photo-low) 100%);
    border-radius: 40px 40px 6px 6px;
  }
  .card--front .photo { left: 520px; top: 18px; width: 200px; height: 416px; }
  .card--back .photo { left: 70px; top: 190px; width: 240px; height: 244px; }

  .name {
    position: absolute;
    font-family: "Cinzel", serif;
    font-weight: 400;
    letter-spacing: 2px;
    line-height: 1.05;
    text-transform: uppercase;
  }
  .card--front .name { left: 40px; top: 66px; color: var(--teal); font-size: 38px; }
  .card--front .name span:last-child { padding-left: 60px; }
  .card--back .name { left: 420px; top: 36px; color: var(--ink-white); font-size: 38px; text-align: center; }
  .name span { display: block; }

  .services {
    position: absolute; left: 36px; top: 226px;
    list-style: none;
    font-family: "Comfortaa", sans-serif;
    font-size: 16.5px; line-height: 25px;
    color: var(--ink-white);
  }
  .services li::before {
    content: "\203A";
    display: inline-block; width: 20px;
    font-weight: 700; color: #222;
  }

  .contact {
    position: absolute; left: 452px; top: 272px;
    list-style: none;
    font-family: "Comfortaa", sans-serif;
    font-size: 17px; color: var(--teal);
  }
  .contact li { display: flex; align-items: center; gap: 12px; height: 44px; }
  .contact svg { width: 24px; height: 26px; flex: none; }
</style>
</head>
<body>
<main class="canvas">

  <section class="card card--front" aria-label="Business card front">
    <div class="background-pattern" role="img" aria-label="Soft pastel triangle pattern background"></div>
    <svg class="shapes" viewBox="0 0 760 434" aria-hidden="true">
      <polygon class="service-band" points="0,208 560,146 560,380 0,424" fill="#0e8ea8"/>
      <polygon class="band-fold" points="470,156 560,146 560,186" fill="#0a7489"/>
    </svg>
    <div class="photo" role="img" aria-label="Photo of the trainer flexing in a red tank top and cap"></div>
    <h1 class="name"><span>Dorinda</span><span>Valcourt</span></h1>
    <ul class="services">
      <li>Personal Fitness Trainer</li>
      <li>Sports Nutritionist</li>
      <li>Individual and Group rates available</li>
      <li>Certifications</li>
      <li>Global Wellness Coaches Federation</li>
      <li>Worldwide Athletic Study Council</li>
    </ul>
  </section>

  <section class="card card--back" aria-label="Business card back">
    <div class="background-pattern" role="img" aria-label="Soft pastel triangle pattern background"></div>
    <svg class="shapes" viewBox="0 0 760 434" aria-hidden="true">
      <polygon class="name-panel" points="330,0 760,0 760,140 130,250" fill="#0e8ea8"/>
    </svg>
    <div class="photo" role="img" aria-label="Photo of the trainer flexing in a red tank top and cap"></div>
    <h2 class="name"><span>Dorinda</span><span>Valcourt</span></h2>
    <ul class="contact">
      <li>
        <svg viewBox="0 0 24 26" aria-hidden="true">
          <polygon points="12,0 24,6.5 24,19.5 12,26 0,19.5 0,6.5" fill="#0e8ea8"/>
          <path d="M8.5 7.5c1 0 1.6 2.4 1 3-.5.4-.8.7-.3 1.6.6 1 1.6 2 2.6 2.6.9.5 1.2.2 1.6-.3.6-.6 3 0 3 1 0 1.3-1.3 2.4-2.6 2.1-3.2-.7-6.300-3.8-7-7-.3-1.3.8-3 1.7-3z" fill="#fff"/>
        </svg>
        555-284-7160
      </li>
      <li>
        <svg viewBox="0 0 24 26" aria-hidden="true">
          <polygon points="12,0 24,6.5 24,19.5 12,26 0,19.5 0,6.5" fill="#0e8ea8"/>
          <rect x="6" y="9" width="12" height="8" fill="#fff"/>
          <polyline points="6,9 12,14 18,9" fill="none" stroke="#0e8ea8" stroke-width="1.2"/>
        </svg>
        dvalcourt4@brimfeld.com
      </li>
    </ul>
  </section>

</main>
</body>
</html>
```